Design of business signage for outside store front

We need signage designed for outside a store front.  We already have a logo, colours and font that we would like to use but would like some ideas as regards layout/design of the signage.  The final product will be for the use of the installer to produce and install the signage.  Attached are files with our logo and font and a picture of the current signage which needs to be replaced.  The size and shape of the signage will be the same as the current signage, its just the design/layout that we would like changed.
N.B. We would like two versions if possible, one with the web address and one without the web address to see what they look like.

```html
<!DOCTYPE html>
<html lang="en">
<head>
<meta charset="utf-8">
<title>Mesa Ibera – Storefront Signage Options</title>
<link href="https://fonts.googleapis.com/css2?family=Cinzel:wght@400&family=Montserrat:wght@400&display=swap" rel="stylesheet">
<style>
  :root {
    --page: #ffffff;
    --sign-dark: #35141a;
    --sign-red: #8b2835;
    --gold: #f2cc30;
    --ivory: #ffffff;
  }
  * { margin: 0; padding: 0; box-sizing: border-box; }
  html, body {
    width: 1200px;
    height: 881px;
    overflow: hidden;
    background: var(--page);
  }
  .canvas {
    position: relative;
    width: 1200px;
    height: 881px;
  }
  .sign {
    position: absolute;
    top: 109px;
    width: 518px;
    height: 215px;
    background: var(--sign-dark);
  }
  .sign--plain { left: 46px; }
  .sign--web { left: 641px; }
  .sign__mark-panel {
    position: absolute;
    left: 36px;
    top: 0;
    width: 135px;
    height: 100%;
    background: var(--sign-red);
  }
  .sign__text {
    position: absolute;
    right: 37px;
    top: 0;
    height: 100%;
    width: 300px;
    text-align: right;
    color: var(--ivory);
  }
  .sign__url {
    position: absolute;
    right: 49px;
    top: 86px;
    font-family: "Montserrat", sans-serif;
    font-size: 10px;
    letter-spacing: 0.2px;
    color: var(--ivory);
    white-space: nowrap;
  }
  .sign__url-name { color: var(--gold); }
  .sign__name {
    position: absolute;
    right: 0;
    top: 99px;
    font-family: "Cinzel", serif;
    font-weight: 400;
    color: var(--ivory);
    text-align: right;
    line-height: 1;
  }
  .sign__name-top {
    display: block;
    font-size: 40px;
    letter-spacing: 1px;
  }
  .sign__name-bottom {
    display: block;
    margin-top: 6px;
    font-size: 24px;
    letter-spacing: 18px;
    margin-right: -18px;
  }
  .sign__tagline {
    position: absolute;
    right: -2px;
    top: 171px;
    font-family: "Montserrat", sans-serif;
    font-size: 10px;
    letter-spacing: 3.2px;
    color: var(--ivory);
    white-space: nowrap;
  }
</style>
</head>
<body>
<main class="canvas">

  <section class="sign sign--plain" aria-label="Sign option without web address">
    <div class="sign__mark-panel"></div>
    <div class="sign__text">
      <p class="sign__name">
        <span class="sign__name-top">MESA</span>
        <span class="sign__name-bottom">IBERA</span>
      </p>
      <p class="sign__tagline">Spanish Artisan Foods</p>
    </div>
  </section>

  <section class="sign sign--web" aria-label="Sign option with web address">
    <div class="sign__mark-panel"></div>
    <div class="sign__text">
      <p class="sign__url">www.<span class="sign__url-name">mesaibera</span>.com.au</p>
      <p class="sign__name">
        <span class="sign__name-top">MESA</span>
        <span class="sign__name-bottom">IBERA</span>
      </p>
      <p class="sign__tagline">Spanish Artisan Foods</p>
    </div>
  </section>

</main>
</body>
</html>
```